Real Estate agent needs flyer/folder to contain bio and overview of services

I'm including files of the layout of the small folder. The folder is 6 1/2 across and 9 1/2 inches long. It will have a front & back cover and then writing on the 2 inside pages.

I am sending a few files to incorporate into the flyer, 1 new logo to use and 2 files which are coloring ideas.

```html
<!DOCTYPE html>
<html lang="en">
<head>
<meta charset="utf-8">
<title>Marisa Calloway – Realtor Folder</title>
<link rel="stylesheet" href="https://fonts.googleapis.com/css2?family=Noto+Serif:wght@400;700&family=PT+Sans:ital,wght@0,400;0,700;1,400;1,700&display=swap">
<style>
  :root {
    --bg: #e4e4e4;
    --navy: #1d4593;
    --navy-2: #2a67b5;
    --sky: #1678c4;
    --sky-2: #0f6db8;
    --ink: #1a1a1a;
    --heading: #1e3f8f;
    --white: #ffffff;
    --paper-shade: #f1f2f4;
    --photo-green: #6f8f4a;
    --photo-water: #8fa7a0;
    --photo-night: #243a66;
    --photo-glow: #c8a86a;
  }
  * { box-sizing: border-box; margin: 0; padding: 0; }
  html, body { width: 1200px; height: 750px; overflow: hidden; }
  body { background: var(--bg); font-family: "PT Sans", sans-serif; color: var(--ink); position: relative; }

  .spread { position: absolute; top: 170px; width: 570px; height: 410px; box-shadow: 0 6px 18px rgba(0,0,0,.18); background: var(--white); }
  .spread--outside { left: 20px; }
  .spread--inside { left: 610px; }
  .page { position: absolute; top: 0; width: 285px; height: 410px; overflow: hidden; }
  .page--left { left: 0; }
  .page--right { left: 285px; }

  .band { position: absolute; left: 0; width: 100%; }
  .band--top { top: 0; height: 162px; }
  .band--photo { top: 162px; height: 92px; }
  .band--bottom { top: 254px; height: 156px; }

  .fill-navy { background: linear-gradient(160deg, var(--navy) 0%, var(--navy-2) 100%); color: var(--white); }
  .fill-sky { background: linear-gradient(160deg, var(--sky) 0%, var(--sky-2) 100%); color: var(--white); }
  .fill-paper { background: linear-gradient(180deg, var(--white) 0%, var(--paper-shade) 100%); }

  .photo { position: absolute; top: 0; height: 100%; }
  .photo--estate { background: linear-gradient(180deg, #7f9c5e 0%, var(--photo-green) 45%, var(--photo-water) 100%); }
  .photo--pool { background: linear-gradient(180deg, var(--photo-night) 0%, var(--photo-glow) 55%, #2f5fa3 100%); }
  .photo--interior { background: linear-gradient(160deg, #3a2e26 0%, #8a6a4c 50%, #d9d4cc 100%); }
  .photo--portrait { background: linear-gradient(180deg, #dcdcdc 0%, #9a8a70 60%, #2a2a2a 100%); }

  .copy { font-size: 5.4px; line-height: 1.38; }
  .copy p + p { margin-top: 4px; }
  .cite { font-style: italic; font-weight: 700; margin-top: 4px; font-size: 5.2px; }
  .head { font-family: "Noto Serif", serif; font-weight: 700; color: var(--heading); font-size: 7.4px; line-height: 1.2; margin-bottom: 3px; }
  .head--light { color: var(--white); }
  .head--intro { font-weight: 400; font-size: 9px; color: var(--white); margin-bottom: 5px; }
  .sub { font-weight: 700; font-size: 5.4px; margin-bottom: 4px; }

  .testimonials { position: absolute; top: 42px; left: 20px; right: 20px; display: flex; gap: 10px; }
  .testimonials .col { flex: 1; }
  .testimonials .col:last-child { margin-top: 8px; }
  .testimonials .head { font-size: 6.8px; margin-bottom: 2px; }

  .contact { position: absolute; top: 12px; left: 0; right: 0; text-align: center; }
  .contact-lead { font-size: 6.2px; line-height: 1.35; padding: 0 34px; margin-bottom: 10px; }
  .contact-list { list-style: none; font-size: 6.6px; line-height: 1.35; color: var(--heading); }
  .brokerage { position: absolute; left: 0; right: 0; bottom: 26px; display: flex; align-items: center; justify-content: center; gap: 5px; font-size: 7.5px; font-weight: 700; color: var(--heading); }
  .brokerage-mark { width: 7px; height: 7px; background: var(--sky); }

  .brand { position: absolute; top: 0; left: 0; right: 0; height: 162px; display: flex; align-items: center; justify-content: center; gap: 7px; }
  .brand-mark { width: 12px; height: 12px; background: var(--heading); }
  .brand-name { font-family: "Noto Serif", serif; font-size: 17px; color: var(--heading); font-weight: 400; }

  .tagline { position: absolute; top: 40px; left: 0; right: 0; text-align: center; font-family: "Noto Serif", serif; font-size: 10.5px; line-height: 1.25; color: var(--white); }

  .intro { position: absolute; top: 36px; left: 26px; right: 22px; }
  .intro .photo--portrait { position: absolute; top: -36px; right: 8px; width: 40px; height: 44px; }

  .two-col { position: absolute; left: 26px; right: 16px; display: flex; gap: 12px; }
  .two-col .col { flex: 1; }
  .two-col--top { top: 40px; }
  .two-col--bottom { top: 18px; }
</style>
</head>
<body>

<section class="spread spread--outside">
  <article class="page page--left back-cover">
    <div class="band band--top fill-navy" style="height:254px;">
      <div class="testimonials">
        <div class="col copy">
          <h3 class="head head--light">Testimonials:</h3>
          <p>During the home buying process, Marisa becomes your trusted advisor, mentor and friend. Her knowledge of the industry, community and market are best in class. A true professional! Marisa aligned her goals with my own and understood the motivation behind my purchase. Marisa is unequivocally the reason why I was able to purchase my home in Laguna Niguel and provide my family with a world-class community. Without her guidance and experience, I would still be in the market attempting to navigate the ever-changing work of real estate.</p>
          <p class="cite">Dana Whitfield</p>
        </div>
        <div class="col copy">
          <p>Marisa is the kind of Real Estate professional everyone wants to represent them. She is knowledgeable, ethical, energetic, and follows up on every detail. Her honesty, integrity and expertise combined make her a very special and remarkable professional. We were lucky to find her!</p>
          <p class="cite">Grant &amp; Elise Morrow</p>
          <p style="margin-top:12px;">Marisa got us an amazing deal on our new home and sold our old home in a week. Marisa is patient, hardworking, professional and most importantly HONEST. Marisa is definitely one of the best in the business!</p>
          <p class="cite">Tessa &amp; Owen Hale</p>
        </div>
      </div>
    </div>
    <div class="band band--bottom fill-paper">
      <div class="contact">
        <p class="contact-lead">Along with being your Realtor, I’m a lifelong resource for all things home-related &amp; beyond… if you need a great referral for anything at all, call me! I can’t wait to work with you!</p>
        <ul class="contact-list">
          <li>Marisa Calloway</li>
          <li>555 014 2287</li>
          <li>marisa@callowayhomes.example</li>
          <li>www.callowayhomes.example</li>
        </ul>
      </div>
      <div class="brokerage"><span class="brokerage-mark"></span><span>Keystone Realty</span></div>
    </div>
  </article>

  <article class="page page--right front-cover">
    <div class="band band--top" style="background:var(--white);">
      <div class="brand"><span class="brand-mark"></span><span class="brand-name">Marisa Calloway</span></div>
    </div>
    <div class="band band--photo">
      <div class="photo photo--estate" style="left:0;width:100%;" role="img" aria-label="Community entrance with fountain pond, palm trees and Mediterranean-style homes"></div>
    </div>
    <div class="band band--bottom fill-sky">
      <p class="tagline">Helping people sell<br>and purchase homes<br>in Southern California</p>
    </div>
  </article>
</section>

<section class="spread spread--inside">
  <article class="page page--left">
    <div class="band band--top fill-navy">
      <div class="intro copy">
        <div class="photo photo--portrait" role="img" aria-label="Portrait of the agent"></div>
        <h2 class="head head--intro">Let me introduce myself</h2>
        <p>I’m originally from Chicago, but I’m a full-fledged California girl now. I’ve lived and worked in Orange County since 1996. I always say where we live is the next best thing to living on a tropical island. I’ve traveled to many and I’m always happy to come back to my Laguna Niguel home.</p>
        <p>My passion for this area is why I’m in Real Estate. I consider myself incredibly fortunate to sell homes and help people purchase homes in an area that I love with all my heart.</p>
        <p>This passion also carries over in representing my clients with the highest degree of professionalism, enthusiasm and care. My business is built on exceptional customer service and I’m grateful my clients are mostly repeat and referrals.</p>
      </div>
    </div>
    <div class="band band--photo">
      <div class="photo photo--estate" style="left:0;width:100%;" role="img" aria-label="Community entrance with fountain pond, palm trees and Mediterranean-style homes"></div>
    </div>
    <div class="band band--bottom fill-paper">
      <div class="two-col two-col--bottom">
        <div class="col copy">
          <h3 class="head">My Core Tenet</h3>
          <p class="sub">It’s All About YOU!</p>
          <p>My #1 priority is understanding YOUR needs and YOUR objectives. This understanding, along with working diligently on your behalf, means we accomplish your goal whether you’re purchasing your 1st home or selling a home you’ve loved so you can move on to the next chapter of your life.</p>
        </div>
        <div class="col copy">
          <h3 class="head">Real Estate Services<br>&amp; Beyond…</h3>
          <p>Simply put, I help people who are local, relocating and investing, sell and purchase homes in Southern California. For purchases outside of California, I can refer to a network of agents across the country.</p>
          <p>I also provide a team who is dedicated to providing outstanding customer service throughout the transaction. My team includes a network of lenders, title, and escrow officers, in house CPA, stagers, photographers, contractors and more.</p>
        </div>
      </div>
    </div>
  </article>

  <article class="page page--right">
    <div class="band band--top" style="background:var(--white);">
      <div class="two-col two-col--top">
        <div class="col copy">
          <h3 class="head">Selling your home</h3>
          <p>Selling your home is not like any other business transaction. It’s also personal. My priority as your Listing Agent is to guide you through what can be a complicated and sometimes emotional process.</p>
          <p>I place great emphasis on marketing your property with professional photographs, along with harnessing the power of the Internet and the virtual world to reach as many buyers as possible. Your property will be marketed to the public as well as</p>
        </div>
        <div class="col copy">
          <p>to other agents, thus creating maximum exposure of your home.</p>
          <p>When we first meet to discuss selling your home, it’s essential for me to gain an understanding of your unique needs such as timelines, expectations and financial considerations, just to name a few. From there, I begin the process of listing and marketing your home. I lead you through negotiations and more paperwork than you ever care to do, guiding you to the successful closing of your home.</p>
        </div>
      </div>
    </div>
    <div class="band band--photo">
      <div class="photo photo--pool" style="left:0;width:168px;" role="img" aria-label="Luxury home at dusk with lit swimming pool and palm trees"></div>
      <div class="photo photo--interior" style="left:168px;width:117px;" role="img" aria-label="Modern open living room with lounge chairs at night"></div>
    </div>
    <div class="band band--bottom fill-sky">
      <div class="two-col two-col--bottom">
        <div class="col copy">
          <h3 class="head head--light">Buying a home</h3>
          <p>If you’re thinking about buying a home, it’s imperative you have an accomplished, real estate professional by your side to walk you through what is likely the largest purchase of your life.</p>
          <p>To get started, I like to meet with you so we have an opportunity to get to know each other as purchasing a home is a uniquely, personal endeavor. At that time, we can discuss your goals and if it’s a good time for you to purchase a home.</p>
        </div>
        <div class="col copy" style="padding-top:10px;">
          <p>From there, the first step is to obtain a pre-approval from a lender. I’m able to recommend various lenders who can introduce and explain the various loan products available.</p>
          <p>After you’ve been pre-approved, that’s when the fun starts! I guide you through the home buying adventure every step of the way and look forward to handing you the keys to your new home.</p>
        </div>
      </div>
    </div>
  </article>
</section>

</body>
</html>
```